Frameless shower doors web site

Build a web site for information and display past projects. Contact information, type of work done. Customer Reviews. The design purpose is to generate phone calls and email inquirers. Domain name is Southernshowerdoors.comEmail is Brightwaveglassworks@mailvista.com Profile We Love What We Do!Brightwave Bath Panels & Glazing LLC. is committed to excellence in every aspect of our business. We hold a standard of integrity bound by fairness, honesty, and personal responsibility. Our distinction is the quality of service and attention to detail we bring to each project. Above all, we listen to our clients input to provide several design options available from designer glass to hardware. We also service and repair existing shower and tub enclosure. Installation of customer purchased enclosure are available by appointment. and address any concerns.

Target Market(s)

25 to 55 residential customers

Number of Pages Required

4 page

Font styles to use
Sans Serif

Colors

Designer to choose colors to be used in the design.

Requirements
Nice to have
• Looking to drive phone calls for estimating shower projects
Should not have
• Lot of prescriptive words, Clutter

```html
<!DOCTYPE html>
<html lang="en">
<head>
<meta charset="utf-8">
<title>Brightwave Glassworks – Frameless Shower Enclosures</title>
<link rel="stylesheet" href="https://fonts.googleapis.com/css2?family=Montserrat:wght@400;500;600;700;800&display=swap">
<style>
:root{
  --navy:#24407f;
  --band:#4a6aa8;
  --band-deep:#3a5a99;
  --testi:#5b86c0;
  --ink:#111111;
  --body:#444444;
  --white:#ffffff;
  --footer:#050505;
  --footer-text:#9a9a9a;
  --hero-a:#cfe0da;
  --hero-b:#9fb9b1;
}
*{margin:0;padding:0;box-sizing:border-box}
html,body{width:1200px;height:2517px;overflow:hidden}
body{position:relative;background:var(--white);font-family:'Montserrat',sans-serif;color:var(--ink)}
.abs{position:absolute}
.center{text-align:center}

/* hero */
.hero{left:0;top:0;width:1200px;height:514px;background:linear-gradient(120deg,var(--hero-a),var(--hero-b) 55%,#d9e6e1)}
.logo{left:131px;top:26px;display:flex;align-items:center;gap:8px;font-size:26px;font-weight:700;color:var(--navy);letter-spacing:1px}
.logo-dot{width:14px;height:14px;background:var(--navy)}
.phone{left:748px;top:24px;display:flex;align-items:center;gap:10px;font-size:17px;font-weight:600}
.quote-btn{left:898px;top:19px;width:170px;height:36px;border-radius:18px;background:var(--navy);color:var(--white);font-size:12px;font-weight:700;display:flex;align-items:center;justify-content:center}
.nav{left:524px;top:68px;width:544px;display:flex;justify-content:space-between;font-size:11.5px;font-weight:600}
.hero-title{left:0;top:240px;width:1200px;font-size:34px;font-weight:800;line-height:41px;letter-spacing:1px}
.hero-sub{left:300px;top:338px;width:600px;font-size:15px;line-height:20px;color:#222}
.more-btn{left:501px;top:402px;width:198px;height:41px;border-radius:21px;background:var(--navy);color:var(--white);font-size:12.5px;font-weight:700;display:flex;align-items:center;justify-content:center}
.slide-arrow{width:50px;height:50px;border-radius:50%;background:rgba(60,80,120,.7);display:flex;align-items:center;justify-content:center}
.notch{width:0;height:0;border-left:14px solid transparent;border-right:14px solid transparent}

/* welcome */
.section-title{font-size:19px;font-weight:700;letter-spacing:.5px;left:0;width:1200px;text-align:center}
.welcome-text{left:240px;top:613px;width:720px;font-size:11.5px;line-height:21px;color:var(--body);text-align:center}
.welcome-text p+p{margin-top:14px}

/* services */
.services{left:0;top:772px;width:1200px;height:447px;background:linear-gradient(90deg,var(--band-deep),var(--band) 50%,var(--band-deep))}
.services .section-title,.testimonials .section-title{color:var(--white)}
.services-sub{left:340px;top:870px;width:520px;font-size:12px;line-height:20px;color:#e4ebf7}
.service-photo{top:952px;height:175px;border-radius:18px;border:3px solid var(--white)}
.service-label{top:1143px;width:262px;font-size:13.5px;font-weight:600;color:var(--white);letter-spacing:.3px;text-align:center}

/* projects */
.project{background:linear-gradient(160deg,#dcdcd8,#8e8c86)}
.project-title{position:absolute;right:14px;bottom:16px;color:var(--white);font-size:13.5px;font-weight:700;letter-spacing:.4px}

/* testimonials */
.testimonials{left:0;top:1936px;width:1200px;height:356px;background:linear-gradient(90deg,#4a77b3,var(--testi) 50%,#4c79b5)}
.review{top:2067px;width:240px;height:165px;background:var(--white);border-radius:14px;padding:20px 18px}
.quote-mark{position:absolute;left:18px;top:8px;font-size:54px;line-height:54px;color:#b9c8e2;font-family:Georgia,serif}
.review-name{margin-top:18px;margin-left:30px;font-size:13px;font-weight:600;color:#222}
.review-text{margin-top:18px;font-size:11px;line-height:20px;color:var(--body);text-align:justify}
.small-arrow{width:24px;height:24px;border-radius:50%;background:rgba(255,255,255,.45);display:flex;align-items:center;justify-content:center}

/* footer */
.footer{left:0;top:2292px;width:1200px;height:225px;background:var(--footer)}
.footer-logo{left:175px;top:2370px;font-size:26px;font-weight:700;color:var(--navy);display:flex;align-items:center;gap:8px}
.copyright{left:140px;top:2438px;width:230px;font-size:9.5px;line-height:18px;color:#333;text-align:center}
.f-col{top:2368px;display:flex;gap:18px}
.f-head{font-size:12px;font-weight:700;color:var(--footer-text);letter-spacing:.5px}
.f-val{font-size:11px;line-height:25px;color:var(--footer-text);margin-top:6px}
.f-val.big{font-size:15px;font-weight:500}
</style>
</head>
<body>

<!-- hero -->
<section class="abs hero" role="img" aria-label="Bright bathroom with a curved frameless glass shower enclosure and a white pedestal sink"></section>
<div class="abs logo"><span class="logo-dot"></span>BRIGHTWAVE</div>
<div class="abs phone">
  <svg width="14" height="14" viewBox="0 0 24 24"><path fill="#111" d="M6.6 10.8a15 15 0 006.6 6.6l2.2-2.2a1 1 0 011-.25 11.4 11.4 0 003.6.57 1 1 0 011 1V20a1 1 0 01-1 1A17 17 0 013 4a1 1 0 011-1h3.5a1 1 0 011 1c0 1.25.2 2.45.57 3.6a1 1 0 01-.25 1z"/></svg>
  975.555.0142
</div>
<div class="abs quote-btn">REQUEST A QUOTE</div>
<nav class="abs nav"><span>HOME</span><span>WHAT WE DO</span><span>GALLERIES</span><span>ABOUT US</span><span>AREAS WE SERVE</span><span>CONTACT</span></nav>
<h1 class="abs hero-title center">AFFORDABLE FRAMLESS<br>SHOWER ENCLOSURES</h1>
<p class="abs hero-sub center">Must explain to you how all this mistaken idea of denouncing pleasure and praising pain was born and I will give you a completed.</p>
<div class="abs more-btn">MORE DETAILS</div>
<div class="abs slide-arrow" style="left:83px;top:275px"><svg width="12" height="12" viewBox="0 0 12 12"><path d="M8 1L3 6l5 5" stroke="#fff" stroke-width="2" fill="none"/></svg></div>
<div class="abs slide-arrow" style="left:1068px;top:275px"><svg width="12" height="12" viewBox="0 0 12 12"><path d="M4 1l5 5-5 5" stroke="#fff" stroke-width="2" fill="none"/></svg></div>
<div class="abs notch" style="left:586px;top:514px;border-top:12px solid #c5d8d1"></div>

<!-- welcome -->
<h2 class="abs section-title" style="top:566px">WELCOME TO BRIGHTWAVE GLASSWORKS</h2>
<div class="abs welcome-text">
  <p>We are DEDICATED to quality, responsiveness, creativity and cost control. Bigger glass contractors are not shower door experts and chuck in a truck doesn't have a showroom and experience like us. Save money, time and hassles while creating the perfect shower for your home - try us and see.</p>
  <p>For over 25 years, Brightwave Bath Panels &amp; Glazing has provided exceptional shower glass doors and services to Sacramento and surrounding communities with a passionate approach to renovations. As a family-owned business.</p>
</div>

<!-- services -->
<section class="abs services" role="img" aria-label="Blue-tinted bathroom interior backdrop"></section>
<div class="abs notch" style="left:586px;top:772px;border-top:12px solid #fff"></div>
<h2 class="abs section-title" style="top:836px">WHAT WE DO</h2>
<p class="abs services-sub center">We focus on shower doors and enclosures, we also provide everything from mirrors to glass shelving when you purchase a shower door from us.</p>
<div class="abs service-photo" style="left:136px;width:259px;background:linear-gradient(150deg,#c9d3d6,#6f7e86)" role="img" aria-label="Sliding glass shower doors in a tiled bathroom"></div>
<div class="abs service-photo" style="left:477px;width:262px;background:linear-gradient(150deg,#f1efea,#8d8a83)" role="img" aria-label="Frameless glass shower enclosure with black hardware"></div>
<div class="abs service-photo" style="left:809px;width:262px;background:linear-gradient(150deg,#5a5f78,#b39a72)" role="img" aria-label="Custom lit vanity mirror above a bathroom counter"></div>
<div class="abs service-label" style="left:134px">GLASS SHOWER DOORS</div>
<div class="abs service-label" style="left:477px">FRAME LESS ENCLOSURES</div>
<div class="abs service-label" style="left:809px">CUSTOM GLASS &amp; MIRRORS</div>
<div class="abs notch" style="left:586px;top:1219px;border-top:12px solid var(--band-deep)"></div>

<!-- projects -->
<h2 class="abs section-title" style="top:1278px">OUR PROJECTS</h2>
<div class="abs project" style="left:131px;top:1328px;width:299px;height:269px;background:linear-gradient(160deg,#f0f2f3,#a8b3b8)" role="img" aria-label="Project: white tiled shower with glass door"><span class="project-title">PROJECT TITLE</span></div>
<div class="abs project" style="left:449px;top:1328px;width:299px;height:269px;background:linear-gradient(160deg,#efe8dc,#b6a88f)" role="img" aria-label="Project: tub enclosure with glass door"><span class="project-title">PROJECT TITLE</span></div>
<div class="abs project" style="left:770px;top:1328px;width:301px;height:269px;background:linear-gradient(160deg,#c6c8ca,#5d5f62)" role="img" aria-label="Project: marble shower with frameless glass panel"><span class="project-title">PROJECT TITLE</span></div>
<div class="abs project" style="left:131px;top:1621px;width:489px;height:247px;background:linear-gradient(90deg,#a89882,#6c6254 65%,var(--navy) 66%)" role="img" aria-label="Project: beige tiled shower with sliding glass door"><span class="project-title">PROJECT TITLE</span></div>
<div class="abs project" style="left:634px;top:1621px;width:433px;height:247px;background:linear-gradient(160deg,#a7a39b,#4e4a44)" role="img" aria-label="Project: stone tiled shower with niche and glass panel"><span class="project-title">PROJECT TITLE</span></div>

<!-- testimonials -->
<section class="abs testimonials" role="img" aria-label="Blue-tinted bathroom backdrop"></section>
<div class="abs notch" style="left:586px;top:1936px;border-top:12px solid #fff"></div>
<h2 class="abs section-title" style="top:1995px">CLIENTS TESTIMONIALS</h2>
<div class="abs small-arrow" style="left:136px;top:2119px"><svg width="8" height="8" viewBox="0 0 8 8"><path d="M6 0L2 4l4 4" stroke="#fff" stroke-width="1.5" fill="none"/></svg></div>
<div class="abs small-arrow" style="left:1043px;top:2119px"><svg width="8" height="8" viewBox="0 0 8 8"><path d="M2 0l4 4-4 4" stroke="#fff" stroke-width="1.5" fill="none"/></svg></div>
<div class="abs review" style="left:189px"><span class="quote-mark">“</span><div class="review-name">Daniel Whitmore</div><p class="review-text">Lorem ipsum dolor sit amet, consectetuer adipiscing elit. Aenean commodo ligula eget dolor. ligula eget dolor.</p></div>
<div class="abs review" style="left:482px"><span class="quote-mark">“</span><div class="review-name">Laura Pennington</div><p class="review-text">Lorem ipsum dolor sit amet, consectetuer adipiscing elit. Aenean commodo ligula eget dolor. ligula eget dolor.</p></div>
<div class="abs review" style="left:770px"><span class="quote-mark">“</span><div class="review-name">Marcus Ellery</div><p class="review-text">Lorem ipsum dolor sit amet, consectetuer adipiscing elit. Aenean commodo ligula eget dolor. ligula eget dolor.</p></div>

<!-- footer -->
<footer class="abs footer"></footer>
<div class="abs notch" style="left:586px;top:2292px;border-top:12px solid #4c79b5"></div>
<div class="abs footer-logo"><span class="logo-dot"></span>BRIGHTWAVE</div>
<p class="abs copyright">© 2019 All content of this website is copyright of Brightwaveglassworks.com</p>

<div class="abs f-col" style="left:384px">
  <svg width="20" height="22" viewBox="0 0 24 24"><path d="M12 2a7 7 0 00-7 7c0 5 7 13 7 13s7-8 7-13a7 7 0 00-7-7z" stroke="#9a9a9a" stroke-width="1.6" fill="none"/><circle cx="12" cy="9" r="2.5" stroke="#9a9a9a" stroke-width="1.6" fill="none"/></svg>
  <div><div class="f-head">ADDRESS</div><div class="f-val">Registered office address<br>42 Harbor View Lane,<br>Suite 3, Riverton, RV4 8PL</div></div>
</div>
<div class="abs f-col" style="left:629px">
  <svg width="22" height="22" viewBox="0 0 24 24"><path d="M6.6 10.8a15 15 0 006.6 6.6l2.2-2.2a1 1 0 011-.25 11.4 11.4 0 003.6.57 1 1 0 011 1V20a1 1 0 01-1 1A17 17 0 013 4a1 1 0 011-1h3.5a1 1 0 011 1c0 1.25.2 2.45.57 3.6a1 1 0 01-.25 1z" stroke="#9a9a9a" stroke-width="1.4" fill="none"/></svg>
  <div><div class="f-head">CALL</div><div class="f-val big">020 5550 1987</div></div>
</div>
<div class="abs f-col" style="left:830px">
  <svg width="22" height="22" viewBox="0 0 24 24"><path d="M2 11L22 3l-6 18-4-8z M12 13l10-10" stroke="#9a9a9a" stroke-width="1.4" fill="none"/></svg>
  <div><div class="f-head">EMAIL</div><div class="f-val">Brightwaveglassworks@mailvista.com</div></div>
</div>

</body>
</html>
```